Cardiology Practice needs a Heart Scan Order Form

Busy cardiology practice needs an order form for a heart scan test. Sample is attached. One side should have all information noted and the other side should have our physician names (Dorian Velko, MD, L.N. Morvesti, MD, Ovila Brandt, MD, Tomas Velko, MD, and Gerald Pompetti, MD. It should have the map that is uploaded and our demographic information (Crestfield Cardiac PLLC, 712 Harrow Ln. Ste. K, Melrick, TX 77431 along with phone 832-417-2286 and fax 832-417-2287) as well as our web address (crestfieldcardiac.example). Our primary colors are red, black and white. Needs to fit paper size 8 1/2 by 11.

Target Market(s)

Healthcare

Industry/Entity Type

Health Care

Font styles to use
Serif

Colors
ec1f27

Requirements
Must have
• Logo, information listed on sample form, demographics and physician names as well as website.
Nice to have
• Open to suggestions
Should not have
• Physician Pictures

```html
<!DOCTYPE html>
<html lang="en">
<head>
<meta charset="utf-8">
<title>Crestfield Cardiac – Calcium Score Heart Scan Order Form</title>
<link href="https://fonts.googleapis.com/css2?family=Montserrat:wght@500;600;700;800&family=Roboto+Condensed:wght@400;700&display=swap" rel="stylesheet">
<style>
:root{
  --red:#c0303a;
  --ink:#222;
  --paper:#fff;
  --line:#9a9a9a;
  --stage:#7a7a7a;
}
*{box-sizing:border-box;margin:0;padding:0}
html,body{width:1200px;height:893px;overflow:hidden}
body{background:var(--stage);position:relative;font-family:"Roboto Condensed",Arial,sans-serif;color:var(--ink)}
.page{position:absolute;top:81px;width:505px;height:715px;background:var(--paper);overflow:hidden}
.page--front{left:74px}
.page--back{left:626px}
.abs{position:absolute}

.brand-name{font-family:"Montserrat",Arial,sans-serif;font-weight:800;color:var(--red);letter-spacing:.5px;line-height:1}

.front-brand{left:27px;top:40px;display:flex;align-items:center;gap:6px}
.front-brand .dot{width:9px;height:9px;border-radius:50%;background:var(--red)}
.front-brand .brand-name{font-size:14px}
.title-rule{left:150px;top:64px;width:328px;height:1.5px;background:var(--red)}
.title-small{right:27px;top:48px;font-family:"Montserrat",sans-serif;font-weight:600;font-size:13px;letter-spacing:3px}
.title-big{right:27px;top:64px;font-family:"Montserrat",sans-serif;font-weight:800;font-size:23px;color:var(--red);letter-spacing:.5px}

.section-label{left:27px;top:115px;font-weight:700;font-size:12px;color:var(--red)}
.bar{left:27px;width:451px;height:18px;background:var(--red);color:#fff;font-family:"Montserrat",sans-serif;font-weight:700;font-size:10px;padding-left:40px;line-height:18px}

.row{left:27px;width:451px;display:flex;align-items:flex-end;font-size:10.5px;white-space:nowrap;gap:3px}
.fill{flex:1;border-bottom:1px dotted var(--line);height:9px;margin-right:4px}
.fill--w{flex:none}
.check{display:inline-flex;align-items:center;gap:3px;margin-right:10px}
.box{width:9px;height:9px;border:1px solid var(--red)}

.instructions{left:23px;top:406px;width:455px;height:156px;background:var(--red);color:#fff;padding:9px 14px;font-size:7.6px;line-height:1.32}
.instructions ul{list-style:none;margin:6px 0}
.instructions li{position:relative;padding-left:12px}
.instructions li::before{content:"";position:absolute;left:2px;top:2.5px;width:4px;height:4px;background:#fff}

.sign{width:145px;border-top:1.3px solid var(--red);font-size:10px;padding-top:3px}
.ref{left:339px;top:582px;width:139px;border:1px solid #bbb;font-size:7px}
.ref div{height:17px;line-height:17px;padding-left:6px;border-top:1px solid #bbb}
.ref .ref-head{background:var(--red);color:#fff;border-top:none;height:14px;line-height:14px}

.footer-line{left:0;top:674px;width:505px;height:1.5px;background:var(--red)}
.footer{left:0;top:677px;width:505px;height:38px;background:var(--red);color:#fff;text-align:center;font-size:9.5px;line-height:12.5px;padding-top:6px}

.back-brand{left:0;width:505px;top:66px;text-align:center}
.back-brand .brand-name{font-size:28px}
.physicians{left:0;width:505px;top:148px;text-align:center;font-family:"Montserrat",sans-serif;font-weight:700;font-size:15px;color:var(--red);line-height:20.5px}
.map{left:29px;top:238px;width:446px;height:318px;border:2px solid var(--red);border-radius:12px;background:linear-gradient(135deg,#e9e5dc 0%,#ececec 45%,#f3e8c8 100%)}
.contact{left:0;width:505px;top:585px;text-align:center;font-family:"Montserrat",sans-serif;font-weight:500;font-size:13.5px;line-height:18.5px;color:#333}
.web{font-family:"Montserrat",sans-serif;font-weight:700;font-size:15px;padding-top:10px;letter-spacing:.3px}
</style>
</head>
<body>

<section class="page page--front">
  <div class="abs front-brand">
    <span class="dot"></span>
    <div class="brand-name">CRESTFIELD CARDIAC</div>
  </div>
  <div class="abs title-rule"></div>
  <div class="abs title-small">CALCIUM SCORE</div>
  <div class="abs title-big">HEART SCAN</div>

  <div class="abs section-label">TEST SCHEDULE</div>
  <div class="abs row" style="top:127px"><span>Test date:</span><span class="fill fill--w" style="width:88px"></span><span style="margin-left:auto">Test time:</span><span class="fill fill--w" style="width:145px;margin-right:0"></span></div>

  <div class="abs bar" style="top:157px">PATIENT INFORMATION</div>
  <div class="abs row" style="top:183px"><span>Name:</span><span class="fill"></span><span>Mi:</span><span class="fill" style="flex:.5;margin-right:0"></span></div>
  <div class="abs row" style="top:204px"><span>Date of birth:</span><span class="fill"></span><span>Account no:</span><span class="fill" style="flex:1.4;margin-right:0"></span></div>
  <div class="abs row" style="top:224px"><span>Address:</span><span class="fill" style="margin-right:0"></span></div>
  <div class="abs row" style="top:245px"><span>Home phone no:</span><span class="fill"></span><span>Mobile phone no:</span><span class="fill" style="margin-right:0"></span></div>

  <div class="abs bar" style="top:279px">MEDICAL INFORMATION</div>
  <div class="abs row" style="top:305px"><span>Sex:</span><span class="fill"></span><span>Height:</span><span class="fill"></span><span>Weight:</span><span class="fill"></span><span>Race:</span><span class="fill" style="flex:2.5;margin-right:14px"></span></div>
  <div class="abs row" style="top:326px"><span>Diagnosis:</span><span class="fill" style="margin-right:0"></span></div>
  <div class="abs row" style="top:346px;font-size:10px;gap:2px"><span class="box"></span><span>PCI (no. of stents:</span><span class="fill fill--w" style="width:28px;margin:0"></span><span>)</span><span class="box" style="margin-left:6px"></span><span>CABG (no. of vessels:</span><span class="fill fill--w" style="width:32px;margin:0"></span><span>)</span><span class="box" style="margin-left:2px"></span><span>MI (last event:</span><span class="fill fill--w" style="width:44px;margin:0"></span><span>)</span><span class="box" style="margin-left:2px"></span><span>PCM/ICD</span></div>
  <div class="abs row" style="top:366px;gap:0"><span class="check"><span class="box"></span>Diabetes</span><span class="check" style="margin-left:14px"><span class="box"></span>Claustrophobia</span><span class="check" style="margin-left:14px"><span class="box"></span>Asthma</span><span class="check" style="margin-left:14px"><span class="box"></span>Emphysema</span><span class="check" style="margin-left:14px"><span class="box"></span>COPD</span></div>
  <div class="abs row" style="top:386px;gap:0"><span>LMP:</span><span class="fill fill--w" style="width:70px;margin-right:8px"></span><span class="check" style="margin-right:6px"><span class="box"></span>bHCG</span><span class="check" style="margin-right:6px"><span class="box"></span>Tubal ligation</span><span class="check" style="margin-right:6px"><span class="box"></span>Post-menopause &gt; 1 year</span><span class="check" style="margin-right:0"><span class="box"></span>Hysterectomy</span></div>

  <div class="abs instructions">
    <p>Please read the following instructions carefully. You might be rescheduled if any of the following instructions are not met.</p>
    <ul>
      <li>AVOID caffeine containing products (coffee, tea, soda, chocolate, energy drinks, or some over the counter medications) for 4 hours prior to testing.</li>
      <li>AVOID smoking for 4 hours prior to testing.</li>
      <li>AVOID eating or drinking anything except water for 4 hours prior to testing.</li>
      <li>Arrive <u>15 minutes</u> early for your appointment time.</li>
      <li>Wear comfortable clothing. <u>Remove any metal objects</u>, such as jewelry or piercings. Women will be asked to remove bras containing metal underwire.</li>
      <li>Inform your physician or the staff if you are claustrophobic or have a problem staying in restricted environments for any length of time.</li>
      <li>Inform the physician or the staff if you are or think you might be pregnant.</li>
    </ul>
    <p>I hereby acknowledge that the instructions and procedures pertinent to this study were explained thoroughly,<br>I had time to ask questions, and these questions were addressed satisfactorily.</p>
  </div>

  <div class="abs sign" style="left:25px;top:594px">Patient's print name</div>
  <div class="abs sign" style="left:176px;top:594px;width:148px">Patient's signature</div>
  <div class="abs sign" style="left:25px;top:635px">Prescriber's print name</div>
  <div class="abs sign" style="left:176px;top:635px;width:148px">Prescriber's signature</div>
  <div class="abs ref">
    <div class="ref-head">Referring physician contact information</div>
    <div>Order date:</div>
    <div>Tel no:</div>
    <div>Fax no:</div>
  </div>

  <div class="abs footer-line"></div>
  <div class="abs footer">Crestfield Cardiac, PLLC. Visit us at 712 Harrow Ln., Ste. K, Melrick, TX 77431.<br>For appointments or more information on testing, please call (832) 417 2286, or visit crestfieldcardiac.example.</div>
</section>

<section class="page page--back">
  <div class="abs back-brand">
    <div class="brand-name">CRESTFIELD CARDIAC</div>
  </div>
  <div class="abs physicians">
    DORIAN VELKO, M.D. | L.N. MORVESTI, M.D.<br>
    OVILA BRANDT, M.D. | TOMAS VELKO, M.D.<br>
    GERALD POMPETTI, M.D.
  </div>
  <div class="abs map" role="img" aria-label="Street map showing the practice location and nearby roads"></div>
  <div class="abs contact">
    CRESTFIELD CARDIAC PLLC<br>
    712 HARROW LN. STE. K, MELRICK, TX 77431<br>
    PHONE 832-417-2286 &amp; FAX 832-417-2287
  </div>
  <div class="abs footer-line"></div>
  <div class="abs footer web">WWW.CRESTFIELDCARDIAC.EXAMPLE</div>
</section>

</body>
</html>
```